Lawn Company needs design work on a service call flyer!

We are a lawn care company that fertilizes and sprays lawns. This design is meant to be left behind at the customers house after a lawn application has been done too let them know what we have done.

The finished design will be printed on A6 paper (4.1 x 5.8 inches)

I have attached PDF files of the text that I want on the front of the document and the back of the document. I also included a sample design that I had been working on to give some idea what I would like. I don't want the same design, but you can use it as a building block for something new or come up with something entirely different.

FRONT: The front of the design is most important.

BACK: Other then the text the design should be minimal. If possible I would like an outline of the trees in my logo to be a backdrop. I have attached a PDF of the back of my business card as an example

The winning design will be a professional looking document that flows and reflects a lawn care business. Please contact me if you have any questions. I will only pick a design that is better then my current template.

Thank You

Target Market(s)

Lawn Care Customers

Industry/Entity Type

Lawn Care

Requirements
Must have
• 1. Our Logo
• 2. The attached text for the front & back of document
• 3. Our phone number (604-918-4471)
• 4. Our Email address (fenwickturfcare@mailora.net)
Nice to have
• A green theme with flowing graphics
Should not have
• any pictures of houses, people, or tools
• Don't copy the text or design from my design template. It is outdated, is it meant to be an example only

```html
<!DOCTYPE html>
<html lang="en">
<head>
<meta charset="utf-8">
<title>Fenwick Turf Care – Service Call Card</title>
<link href="https://fonts.googleapis.com/css2?family=Source+Sans+3:ital,wght@0,400;0,600;0,700;1,400&display=swap" rel="stylesheet">
<style>
  :root{
    --bg:#c9cec4;
    --leaf:#1f7a1f;
    --leaf-dark:#17611a;
    --leaf-mid:#4fae2a;
    --leaf-light:#8fd14a;
    --lime:#8cc63f;
    --panel:#eef6df;
    --ink:#1d5e1f;
    --white:#ffffff;
    --grass-a:#2f8a2a;
    --grass-b:#5aa938;
  }
  *{box-sizing:border-box;margin:0;padding:0}
  html,body{width:1200px;height:800px;overflow:hidden}
  body{
    background:radial-gradient(ellipse at 60% 40%,#eef0ea 0%,var(--bg) 75%);
    font-family:"Source Sans 3",sans-serif;
    position:relative;
  }
  .card{position:absolute;width:556px;height:394px;box-shadow:0 4px 10px rgba(0,0,0,.35);overflow:hidden}

  /* ---------- back side ---------- */
  .card-back{left:496px;top:282px;background:var(--white)}
  .back-header{height:46px;background:var(--lime);color:var(--white);font-size:14px;padding:13px 0 0 40px}
  .utilize-note{position:absolute;left:35px;top:238px;font-size:8.5px;color:var(--ink)}
  .mowing{position:absolute;left:274px;top:58px;width:262px;color:var(--ink)}
  .mowing h2{font-size:11.5px;font-weight:600;color:var(--leaf-mid);margin-bottom:4px}
  .mowing .lead{font-size:10px;line-height:12.5px;margin-bottom:10px}
  .mowing ul{list-style:none}
  .mowing li{font-size:8.4px;line-height:10.6px;padding-left:14px;position:relative;margin-bottom:3px}
  .mowing li::before{content:"•";position:absolute;left:0;top:0}
  .tree-row{position:absolute;left:172px;top:256px;width:358px;height:88px;
    background:linear-gradient(90deg,rgba(46,130,40,.85),rgba(70,150,50,.9) 50%,rgba(46,130,40,.85));
    border-radius:40px 40px 0 0}
  .contact-band{position:absolute;left:0;bottom:0;width:100%;height:52px;
    background:linear-gradient(180deg,var(--grass-b),var(--grass-a));
    display:flex;align-items:center;color:var(--white);font-size:15px;font-weight:600}
  .contact-item{display:flex;align-items:center;gap:7px;position:absolute}
  .contact-phone{left:80px}
  .contact-email{left:252px;font-size:14px}
  .contact-item svg{width:26px;height:26px}

  /* ---------- front side ---------- */
  .card-front{left:160px;top:136px;
    background:
      radial-gradient(circle at 15% 20%,rgba(210,240,150,.55),transparent 22%),
      radial-gradient(circle at 85% 15%,rgba(220,245,160,.5),transparent 24%),
      radial-gradient(circle at 35% 45%,rgba(190,230,120,.4),transparent 25%),
      linear-gradient(180deg,#5fb32c 0%,#8ccc43 40%,#7ec23a 70%,#3f9625 100%)}
  .ribbon{position:absolute;left:176px;top:0;width:202px;height:280px}
  .ribbon svg{position:absolute;inset:0}
  .ribbon-content{position:absolute;inset:0;text-align:center;color:var(--ink)}
  .brand{margin-top:26px;display:flex;flex-direction:column;align-items:center;gap:6px}
  .brand-dot{width:34px;height:34px;border-radius:50%;background:var(--leaf)}
  .brand-name{font-size:17px;font-weight:700;color:var(--leaf-dark);letter-spacing:.5px}
  .field-label{font-size:14px;font-weight:600;margin-top:34px}
  .field-line{width:148px;height:1px;background:var(--ink);margin:26px auto 0}
  .serviced{font-size:14px;font-weight:600;line-height:16.5px;margin-top:20px}
  .field-line.second{margin-top:24px}

  .applied{position:absolute;left:19px;top:154px;color:var(--ink)}
  .applied h3{font-size:14px;font-weight:400;line-height:18px;margin-bottom:10px}
  .option{display:flex;gap:7px;margin-bottom:7px}
  .box{width:15px;height:15px;background:rgba(255,255,255,.85);flex:none;margin-top:1px}
  .option-text{font-size:12.5px;line-height:15px}
  .option-text small{display:block;font-size:9.5px;line-height:12px}
  .blank{display:inline-block;width:112px;border-bottom:1px solid var(--ink);margin-left:4px}

  .watering{position:absolute;left:42px;top:328px;font-size:12.5px;color:var(--ink)}
  .watering .blank{width:112px;margin:0 2px}

  .promise{position:absolute;left:392px;top:152px;width:152px;font-style:italic;
    font-size:11.3px;line-height:16px;color:var(--white)}
</style>
</head>
<body>

<section class="card card-back" aria-label="Back of service card">
  <header class="back-header">Please follow these general guidelines:</header>
  <p class="utilize-note">utilize more water and prevent unnecessary runoff.</p>

  <article class="mowing">
    <h2>MOWING YOUR LAWN</h2>
    <p class="lead">Mowing your lawn properly can make all the difference in how it looks throughout the year</p>
    <ul>
      <li>You should mow your lawn at 2.5 - 3 inches (no shorter). Mowing at this length helps shade your roots and provides more leaf surface for your lawn to manufacture its own food. As an added bonus it will help your lawn retain its moisture and reduce watering requirements.</li>
      <li>As a general rule, try not to remove more then 1/3 of the leave blade in a single mowing. During periods of heavy growth, this may mean mowing more frequently then usual.</li>
      <li>Always ensure your lawn mower is maintained and the blade is sharp so that is cuts cleanly.</li>
      <li>Your last mowing in the fall should be shorter, about 2 inches.</li>
    </ul>
  </article>

  <div class="tree-row" role="img" aria-label="Row of four green leafy trees through the seasons"></div>

  <footer class="contact-band">
    <span class="contact-item contact-phone">
      <svg viewBox="0 0 26 26" aria-hidden="true"><circle cx="13" cy="13" r="11.5" fill="none" stroke="#fff" stroke-width="2"/><path d="M9 7.5c.6-.5 1.3-.4 1.7.2l1.2 1.9c.3.5.2 1.1-.2 1.5l-.8.7c.6 1.5 1.7 2.7 3.2 3.4l.7-.8c.4-.4 1-.5 1.5-.2l1.9 1.2c.6.4.7 1.1.2 1.7l-.8.9c-.8.8-2 1-3 .5-3-1.4-5.3-3.7-6.6-6.7-.4-1-.2-2.2.5-3z" fill="#fff"/></svg>
      604-918-4471
    </span>
    <span class="contact-item contact-email">
      <svg viewBox="0 0 26 26" aria-hidden="true"><circle cx="13" cy="13" r="11.5" fill="none" stroke="#fff" stroke-width="2"/><rect x="7" y="9" width="12" height="8.5" rx="1" fill="none" stroke="#fff" stroke-width="1.5"/><path d="M7.3 9.5 13 14l5.7-4.5M7.3 17l4-3.6M18.7 17l-4-3.6" fill="none" stroke="#fff" stroke-width="1.3"/></svg>
      fenwickturfcare@mailora.net
    </span>
  </footer>
</section>

<section class="card card-front" aria-label="Front of service card">
  <div class="ribbon">
    <svg viewBox="0 0 202 280" preserveAspectRatio="none" aria-hidden="true">
      <path d="M0 0H202V280L101 252L0 280Z" fill="var(--leaf-mid)"/>
      <path d="M8 0H194V266L101 240L8 266Z" fill="var(--panel)" opacity=".92"/>
    </svg>
    <div class="ribbon-content">
      <div class="brand">
        <span class="brand-dot"></span>
        <span class="brand-name">FENWICK TURF CARE</span>
      </div>
      <p class="field-label">Application Time / Date:</p>
      <div class="field-line"></div>
      <p class="serviced">Your Lawn<br>has been Professionally<br>Serviced today by:</p>
      <div class="field-line second"></div>
    </div>
  </div>

  <div class="applied">
    <h3>Today's application<br>consists of:</h3>
    <div class="option"><span class="box"></span><span class="option-text">Seasonally Balanced<br>Slow Release Fertilizer</span></div>
    <div class="option"><span class="box"></span><span class="option-text">Broadleaf Weed<br>Control<small>(Please keep off the lawn<br>until it is thoroughly dry)</small></span></div>
    <div class="option"><span class="box"></span><span class="option-text">Other:<span class="blank"></span></span></div>
  </div>

  <p class="watering">Please begin watering the lawn<span class="blank"></span>after application.</p>

  <p class="promise">“We strive to complete work in a professional manner each and every visit. If you are not satisfied with the level of service you are receiving please contact us. We value your business and wish to maintain long-term relationships with our customers.”</p>
</section>

</body>
</html>
```